BenQoral Medical

We are a medical supplier company we sell machines and equipment to all medical sectors in Iraq. Our services include not only the installation of these machines and equipment but also we provide support after installation and we train the staff to use these machines/equipment
We need a website that will make us stand out from our competitors, something professional and catchy
Starting from the home page, before showing the home page we want the loading screen to have our logo animated in a nice way
Then we can proceed to creating the other pages which are
Projects
Services
Training
About
and Contact us
Attached below is our logo and the color blue that we hope to use in the theme of the website
**** In the home page we want to focus on our partners and services****

Target Market(s)

Medical Sector

Industry/Entity Type

Medical

Coding

Coded - Design and coding required

Number of Pages Required

5+ page

Colors
0054AA
0677BA
7BADD7
CADEEF
E8F1F8

Requirements
Must have
• Animation in loading screen or animation in home page
Nice to have
• Some sort of animation for our partners

```html
<!DOCTYPE html>
<html lang="en">
<head>
<meta charset="utf-8">
<title>BenQoral Medical – Medical Equipment Suppliers</title>
<link href="https://fonts.googleapis.com/css2?family=Open+Sans:wght@400;500;600;700;800&display=swap" rel="stylesheet">
<style>
:root{
  --blue-dark:#0054AA;
  --blue:#0677BA;
  --blue-mid:#7BADD7;
  --blue-soft:#CADEEF;
  --blue-pale:#E8F1F8;
  --ink:#111111;
  --text:#333333;
  --muted:#666666;
  --footer:#0d2132;
  --white:#ffffff;
  --gold:#f5b50a;
}
*{margin:0;padding:0;box-sizing:border-box}
html,body{width:1200px;height:4141px;overflow:hidden}
body{position:relative;background:var(--white);font-family:"Open Sans",Arial,sans-serif;color:var(--text)}
.abs{position:absolute}
a{color:inherit;text-decoration:none}

/* header */
.site-header{position:absolute;left:0;top:0;width:1200px;height:90px;background:var(--white)}
.brand{position:absolute;left:141px;top:22px;display:flex;align-items:center;gap:12px}
.brand-mark{width:40px;height:40px;border:5px solid var(--blue)}
.brand-name{font-size:34px;font-weight:700;color:var(--blue-dark);line-height:1}
.main-nav{position:absolute;left:511px;top:33px;display:flex;gap:24px;font-size:13px;font-weight:500;color:var(--ink)}
.main-nav .active{color:var(--blue);border-bottom:1px solid var(--blue)}
.btn{display:inline-flex;align-items:center;justify-content:center;background:var(--blue);color:var(--white);border-radius:30px;font-weight:600}
.header-cta{position:absolute;left:933px;top:23px;width:125px;height:42px;font-size:13px}

/* hero */
.hero{position:absolute;left:0;top:90px;width:1200px;height:600px;background:linear-gradient(100deg,#0f2c45 0%,#3c5e78 35%,#8fb0c8 70%,#c9dbe8 100%)}
.hero-title{position:absolute;left:141px;top:120px;font-size:50px;font-weight:800;color:var(--white);line-height:61px;letter-spacing:1px}
.hero-sub{position:absolute;left:141px;top:258px;font-size:17px;color:var(--white)}
.hero-btn{position:absolute;left:141px;top:311px;width:125px;height:42px;font-size:13px}
.wave{position:absolute;left:0}

/* about */
.about-photo{position:absolute;left:141px;top:780px;width:430px;height:326px;background:linear-gradient(135deg,#dfe8ef,#f4f7fa 50%,#c5d3de);border:12px solid #2a9ad8}
.eyebrow{position:absolute;left:628px;top:773px;font-size:17px;color:var(--blue-dark)}
.about-title{position:absolute;left:628px;top:803px;font-size:22px;font-weight:600;color:var(--ink)}
.about-text{position:absolute;left:628px;width:430px;font-size:13px;line-height:22.5px;color:var(--text)}
.about-btn{position:absolute;left:628px;top:1068px;width:126px;height:42px;font-size:13px}

/* sections */
.section-title{position:absolute;left:0;width:1200px;text-align:center;font-size:35px;font-weight:600;color:var(--ink)}
.partners{position:absolute;left:137px;top:1470px;width:926px;display:flex;justify-content:space-between;align-items:center}
.partner{display:flex;align-items:center;gap:10px}
.partner-shape{width:62px;height:62px;border-radius:50%;background:var(--blue-soft)}
.partner-shape.square{border-radius:8px}
.partner-bar{width:86px;height:14px;border-radius:7px;background:var(--blue-pale)}

.service-card{position:absolute;top:1773px;width:293px;height:310px;background:var(--blue-pale);border-radius:28px;text-align:center}
.service-icon{position:absolute;left:98px;top:45px;width:97px;height:97px;border-radius:50%;background:var(--blue);display:flex;align-items:center;justify-content:center}
.service-name{position:absolute;left:0;top:160px;width:100%;font-size:18px;font-weight:600;color:var(--ink)}
.service-text{position:absolute;left:30px;top:193px;width:233px;font-size:11.5px;line-height:19px;color:var(--text)}
.read-more{position:absolute;left:0;top:260px;width:100%;font-size:13px;color:var(--blue);text-decoration:underline}

.project-card{position:absolute;top:2248px;width:294px;height:245px;border-radius:12px;overflow:hidden}
.project-photo{position:absolute;inset:0;background:linear-gradient(160deg,#cfe0ee,#7da4c2 60%,#2b4960)}
.project-card .shade{position:absolute;inset:0;background:linear-gradient(to bottom,rgba(0,0,0,0) 45%,rgba(0,0,0,.55))}
.project-caption{position:absolute;left:20px;bottom:25px;width:254px;text-align:center;font-size:12px;line-height:20px;color:var(--white)}
.view-btn{position:absolute;left:507px;top:2546px;width:186px;height:46px;font-size:14px}

/* testimonials */
.review{position:absolute;top:2945px;width:428px;height:241px;background:#f7f9fb;border-radius:12px;box-shadow:0 4px 18px rgba(0,0,0,.06)}
.review.front{background:var(--white)}
.avatar{position:absolute;left:18px;top:36px;width:58px;height:58px;border-radius:50%;background:linear-gradient(#b89a86,#e4d4c8)}
.stars{position:absolute;left:92px;top:30px;font-size:13px;letter-spacing:1px;color:var(--gold)}
.reviewer{position:absolute;left:92px;top:48px;font-size:23px;font-weight:600;color:var(--ink)}
.role{position:absolute;left:92px;top:80px;font-size:14px;color:var(--muted)}
.source-dot{position:absolute;right:40px;top:30px;width:30px;height:30px;border-radius:50%;border:4px solid var(--blue-soft)}
.quote{position:absolute;left:92px;top:113px;width:310px;font-size:13.5px;line-height:22.5px;color:var(--muted)}
.arrow-btn{position:absolute;left:62px;top:3041px;width:53px;height:53px;border-radius:50%;border:1.5px solid var(--ink);display:flex;align-items:center;justify-content:center}

/* cta */
.cta{position:absolute;left:141px;top:3283px;width:917px;height:301px;border-radius:28px;background:linear-gradient(120deg,#1a7fc3,#2f8ed0 50%,#1673b4)}
.cta-title{position:absolute;left:0;top:70px;width:100%;text-align:center;font-size:34px;font-weight:600;line-height:46px;color:var(--white)}
.cta-btn{position:absolute;left:389px;top:181px;width:140px;height:42px;background:var(--white);color:var(--blue);font-size:13px;font-weight:500}

/* footer */
.site-footer{position:absolute;left:0;top:3680px;width:1200px;height:461px}
.footer-nav{position:absolute;left:326px;top:208px;display:flex;gap:37px;font-size:13px;color:var(--white)}
.footer-nav .active{color:var(--blue)}
.footer-rule{position:absolute;left:141px;width:917px;height:1px;background:rgba(255,255,255,.2)}
.footer-brand{position:absolute;left:137px;top:290px;display:flex;align-items:center;gap:12px}
.footer-brand .brand-mark{border-color:var(--white)}
.footer-brand .brand-name{color:var(--white)}
.footer-info{position:absolute;top:297px;display:flex;gap:10px;font-size:13px;line-height:22px;color:var(--white)}
.footer-sep{position:absolute;top:282px;width:1px;height:66px;background:rgba(255,255,255,.25)}
.copyright{position:absolute;left:141px;top:414px;font-size:12.5px;color:var(--white)}
.social{position:absolute;top:413px;width:22px;height:22px;border-radius:50%;background:var(--blue)}
</style>
</head>
<body>

<header class="site-header">
  <div class="brand"><span class="brand-mark"></span><span class="brand-name">BenQoral</span></div>
  <nav class="main-nav">
    <a class="active">Home</a><a>About Us</a><a>Services</a><a>Featured Projects</a><a>Training</a>
  </nav>
  <a class="btn header-cta">Contact Us</a>
</header>

<section class="hero">
  <div class="abs" style="inset:0" role="img" aria-label="Photo of a modern operating room with surgical lights and an operating table"></div>
  <h1 class="hero-title">EMPOWERING<br>MEDICAL EXCELLENCE</h1>
  <p class="hero-sub">Your trusted partner for medical equipment and services</p>
  <a class="btn hero-btn">Learn More</a>
</section>

<svg class="wave" style="top:560px" width="1200" height="170" viewBox="0 0 1200 170">
  <path d="M0 130 C140 40 380 20 600 85 C740 125 820 112 930 100 C1050 88 1140 50 1200 20 L1200 170 L0 170Z" fill="#fff"/>
  <path d="M0 120 C140 30 380 10 600 75 C700 103 760 108 800 106 C700 110 660 100 600 88 C380 35 150 60 0 140Z" fill="#0677BA"/>
  <path d="M680 112 C820 115 1000 110 1200 10" stroke="#0677BA" stroke-width="5" fill="none"/>
</svg>
<svg class="abs" style="left:622px;top:614px" width="72" height="72"><circle cx="36" cy="36" r="29" fill="#fff" stroke="#0677BA" stroke-width="11"/></svg>

<section class="about">
  <div class="about-photo" role="img" aria-label="Photo of a clinical equipment room framed by the company initial"></div>
  <p class="eyebrow">About Us</p>
  <h2 class="about-title">BenQoral Medical Equipments Suppliers</h2>
  <p class="about-text" style="top:847px">Lorem ipsum dolor sit amet, consectetur adipiscing elit, sed do eiusmod tempor incididunt ut labore et dolore magna aliqua. Quis ipsum suspendisse ultrices gravida. Risus commodo viverra maecenas accumsan lacus vel facilisis</p>
  <p class="about-text" style="top:960px">Lorem ipsum dolor sit amet, consectetur adipiscing elit, sed do eiusmod tempor incididunt ut labore et dolore magna aliqua. Quis ipsum suspendisse ultrices gravida. Risus commodo viverra maecenas accumsan lacus vel facilisis.</p>
  <a class="btn about-btn">Learn More</a>
</section>

<svg class="wave" style="top:1200px" width="1200" height="125" viewBox="0 0 1200 125">
  <path d="M295 28 C420 16 520 24 600 52 C760 120 1000 125 1200 12 L1200 32 C1000 140 760 132 600 64 C520 34 420 26 295 28Z" fill="#0677BA"/>
</svg>
<svg class="abs" style="left:502px;top:1205px" width="72" height="72"><circle cx="36" cy="36" r="29" fill="#fff" stroke="#0677BA" stroke-width="11"/></svg>

<h2 class="section-title" style="top:1370px">Our Partner</h2>
<div class="partners">
  <div class="partner"><span class="partner-shape"></span><span class="partner-bar"></span></div>
  <div class="partner"><span class="partner-shape square"></span><span class="partner-bar"></span></div>
  <div class="partner"><span class="partner-shape"></span><span class="partner-bar"></span></div>
  <div class="partner"><span class="partner-shape square"></span><span class="partner-bar"></span></div>
  <div class="partner"><span class="partner-shape"></span><span class="partner-bar"></span></div>
</div>

<h2 class="section-title" style="top:1683px">Our Services</h2>
<article class="service-card" style="left:141px">
  <div class="service-icon"><svg width="48" height="48" viewBox="0 0 48 48" fill="none" stroke="#fff" stroke-width="3" stroke-linecap="round"><path d="M14 8v10a9 9 0 0 0 18 0V8"/><path d="M23 27v5a8 8 0 0 0 16 0v-4"/><circle cx="39" cy="24" r="4"/></svg></div>
  <h3 class="service-name">Stethoscope</h3>
  <p class="service-text">Lorem ipsum dolor sit amet, consectetur adipiscing elit, sed do eiusmod incididunt ut labore.</p>
  <a class="read-more">Read More</a>
</article>
<article class="service-card" style="left:453px">
  <div class="service-icon"><svg width="48" height="48" viewBox="0 0 48 48" fill="none" stroke="#fff" stroke-width="3" stroke-linecap="round"><circle cx="24" cy="24" r="13"/><circle cx="24" cy="24" r="5"/><path d="M24 5v6M24 37v6M5 24h6M37 24h6M11 11l4 4M33 33l4 4M37 11l-4 4M11 37l4-4"/></svg></div>
  <h3 class="service-name">Wrench</h3>
  <p class="service-text">Lorem ipsum dolor sit amet, consectetur adipiscing elit, sed do eiusmod incididunt ut labore.</p>
  <a class="read-more">Read More</a>
</article>
<article class="service-card" style="left:764px">
  <div class="service-icon"><svg width="48" height="48" viewBox="0 0 48 48" fill="#fff"><path d="M6 12c6-2 12-1 17 2v24c-5-3-11-4-17-2z"/><path d="M42 12c-6-2-12-1-17 2v24c5-3 11-4 17-2z"/></svg></div>
  <h3 class="service-name">Book</h3>
  <p class="service-text">Lorem ipsum dolor sit amet, consectetur adipiscing elit, sed do eiusmod incididunt ut labore.</p>
  <a class="read-more">Read More</a>
</article>

<h2 class="section-title" style="top:2158px">Featured Projects</h2>
<article class="project-card" style="left:142px">
  <div class="project-photo" role="img" aria-label="Photo of a patient entering an MRI scanner"></div><div class="shade"></div>
  <p class="project-caption">Lorem ipsum dolor sit amet, consectetur incididunt ut labore et.</p>
</article>
<article class="project-card" style="left:453px">
  <div class="project-photo" role="img" aria-label="Photo of a laboratory microscope"></div><div class="shade"></div>
  <p class="project-caption">Lorem ipsum dolor sit amet, consectetur incididunt ut labore et.</p>
</article>
<article class="project-card" style="left:763px">
  <div class="project-photo" role="img" aria-label="Photo of an equipped examination room"></div><div class="shade"></div>
  <p class="project-caption">Lorem ipsum dolor sit amet, consectetur incididunt ut labore et.</p>
</article>
<a class="btn view-btn">View All products</a>

<svg class="wave" style="top:2680px" width="1200" height="125" viewBox="0 0 1200 125">
  <path d="M0 20 C200 110 440 120 600 62 C680 36 780 30 905 32 C780 38 680 50 600 76 C440 135 200 125 0 40Z" fill="#0677BA"/>
</svg>
<svg class="abs" style="left:622px;top:2686px" width="72" height="72"><circle cx="36" cy="36" r="29" fill="#fff" stroke="#0677BA" stroke-width="11"/></svg>

<h2 class="section-title" style="top:2855px">What Client Say About Us</h2>
<a class="arrow-btn"><svg width="20" height="16" viewBox="0 0 20 16" fill="none" stroke="#111" stroke-width="2" stroke-linecap="round"><path d="M19 8H2M8 2L2 8l6 6"/></svg></a>
<article class="review front" style="left:173px">
  <div class="avatar" role="img" aria-label="Client portrait"></div>
  <span class="stars">★★★★★</span><span class="source-dot"></span>
  <h3 class="reviewer">Laith Karim</h3><p class="role">Client Profession</p>
  <p class="quote">Lorem ipsum dolor sit amet, consectetur ip-sadipss isicing elit, sed do eiusmod tempor i ncidi dunt labore et dolore magna aliqua. sss Ut enim adispgd minim veniam,</p>
</article>
<article class="review" style="left:634px">
  <div class="avatar" role="img" aria-label="Client portrait"></div>
  <span class="stars">★★★★★</span><span class="source-dot"></span>
  <h3 class="reviewer">Laith Karim</h3><p class="role">Client Profession</p>
  <p class="quote">Lorem ipsum dolor sit amet, consectetur ip-sadipss isicing elit, sed do eiusmod tempor i ncidi dunt labore et dolore magna aliqua. sss Ut enim adispgd minim veniam,</p>
</article>
<article class="review" style="left:1092px">
  <div class="avatar" role="img" aria-label="Client portrait"></div>
  <span class="stars">★★★★★</span>
  <h3 class="reviewer">Laith Karim</h3><p class="role">Client Profession</p>
  <p class="quote">Lorem ipsum dolor sit amet, consectetur ip-sadipss isicing elit, sed do eiusmod tempor i ncidi dunt labore et dolore magna aliqua. sss Ut enim adispgd minim veniam,</p>
</article>

<section class="cta">
  <div class="abs" style="inset:0;border-radius:28px" role="img" aria-label="Blue-tinted photo of laboratory glassware"></div>
  <h2 class="cta-title">BenQoral Medical Equipments<br>Suppliers</h2>
  <a class="btn cta-btn">Contact Now</a>
</section>

<footer class="site-footer">
  <svg class="abs" style="left:0;top:0" width="1200" height="461" viewBox="0 0 1200 461">
    <defs><linearGradient id="footerFade" x1="0" y1="0" x2="1" y2="1"><stop offset="0" stop-color="#14304a"/><stop offset="1" stop-color="#0a1a28"/></linearGradient></defs>
    <path d="M0 120 C160 60 380 40 538 45 C700 50 800 95 920 95 C1040 95 1130 55 1200 10 L1200 461 L0 461Z" fill="url(#footerFade)"/>
    <path d="M0 112 C160 52 380 30 538 35 C700 42 800 88 920 88 C1040 88 1130 45 1200 0 L1200 18 C1130 62 1040 104 920 104 C800 104 700 60 538 52 C380 48 160 70 0 128Z" fill="#0677BA"/>
  </svg>
  <svg class="abs" style="left:502px;top:5px" width="72" height="72"><circle cx="36" cy="36" r="29" fill="#fff" stroke="#0677BA" stroke-width="11"/></svg>
  <div class="abs" style="left:0;top:130px;width:1200px;height:331px" role="img" aria-label="Faint dark photo of hospital equipment"></div>

  <nav class="footer-nav"><a class="active">Home</a><a>Services</a><a>About Us</a><a>Featured Projects</a><a>Training</a><a>Contact Us</a></nav>
  <div class="footer-rule" style="top:248px"></div>

  <div class="footer-brand"><span class="brand-mark"></span><span class="brand-name">BenQoral</span></div>
  <span class="footer-sep" style="left:386px"></span>
  <div class="footer-info" style="left:418px">
    <svg width="16" height="18" viewBox="0 0 16 18" fill="none" stroke="#fff" stroke-width="1.5"><path d="M8 17s6-6 6-10A6 6 0 0 0 2 7c0 4 6 10 6 10z"/><circle cx="8" cy="7" r="2"/></svg>
    <p>123 Lorem ipsume Dilor<br>Site 32311 Lorem ipsume</p>
  </div>
  <span class="footer-sep" style="left:631px"></span>
  <div class="footer-info" style="left:663px">
    <svg width="18" height="18" viewBox="0 0 18 18" fill="none" stroke="#fff" stroke-width="1.5"><path d="M4 1l3 4-2 2a10 10 0 0 0 6 6l2-2 4 3-2 3C8 17 1 10 1 3z"/></svg>
    <p>Call :<br>123 456 7890</p>
  </div>
  <div class="footer-info" style="left:845px">
    <svg width="18" height="14" viewBox="0 0 18 14" fill="none" stroke="#fff" stroke-width="1.5"><rect x="1" y="1" width="16" height="12" rx="1"/><path d="M1 2l8 6 8-6"/></svg>
    <p>Email :<br>info@benqoralmedical.com</p>
  </div>

  <div class="footer-rule" style="top:390px"></div>
  <p class="copyright">© 2024 BenQoral Medical Equipments Suppliers. All Rights Reserved.</p>
  <span class="social" style="left:975px"></span>
  <span class="social" style="left:1004px"></span>
  <span class="social" style="left:1034px"></span>
</footer>

</body>
</html>
```